A property investment company, looking to provide lovely sustainable homes for familys and individua

For a small investment business i am starting which will buy and refurbish unloved houses and apartments to rent out or resell. the company name is my family surname (HARGREAVE). <br/>i would like the design to be simple with maybe some emphasis on an ethical and sustainable/environmentally friendly approach with a branding of maybe trees blended with some houses and or apartments.<br/>The colours i like for this design would be mainly green on either a white or black background.
Target Market(s)
This business card is to be used for professional people such as estate agents
mortgage brokers, solicitors and trades people.
Industry/Entity Type
Real Estate
Contact Information for Business Card
owner/director-Martin hargreave
e-mail-martin@hvholdings.co.uk
website-hargreavehomeholdings.co.uk
mobile-07700945318
landline-02079460581
Look and feel

```html
<!DOCTYPE html>
<html lang="en">
<head>
<meta charset="utf-8">
<title>Hargreave Business Card</title>
<link href="https://fonts.googleapis.com/css2?family=Cinzel:wght@500;600&family=Crimson+Text:wght@400;600&display=swap" rel="stylesheet">
<style>
  :root {
    --canvas: #2a2a2c;
    --card: #0b0b0c;
    --facet-1: #161617;
    --facet-2: #1f1f21;
    --facet-3: #2b2b2e;
    --green: #8cc63f;
    --white: #f2f2f2;
  }
  * { margin: 0; padding: 0; box-sizing: border-box; }
  html, body { width: 1200px; height: 800px; overflow: hidden; }
  body {
    background: var(--canvas);
    display: flex;
    align-items: center;
    justify-content: center;
    gap: 40px;
  }
  .card {
    position: relative;
    width: 540px;
    height: 309px;
    background: var(--card);
    overflow: hidden;
    box-shadow: 0 18px 40px rgba(0,0,0,.45);
  }
  .card-facets { position: absolute; inset: 0; width: 100%; height: 100%; }
  .card-stripe {
    position: absolute;
    left: 0; right: 0;
    bottom: 14px;
    height: 7px;
    background: var(--green);
  }
  .brand {
    position: absolute;
    display: flex;
    align-items: center;
    gap: 10px;
    font-family: "Cinzel", serif;
    font-weight: 600;
    color: var(--green);
    letter-spacing: 2px;
    white-space: nowrap;
  }
  .brand-mark { width: 13px; height: 13px; background: var(--green); flex: none; }
  .card-front .brand { left: 120px; top: 118px; font-size: 46px; }

  .card-back .brand { left: 34px; top: 186px; font-size: 26px; gap: 9px; }
  .card-back .brand-mark { width: 10px; height: 10px; }
  .divider {
    position: absolute;
    left: 292px; top: 58px;
    width: 1px; height: 120px;
    background: linear-gradient(var(--card), var(--white), var(--card));
  }
  .contact {
    position: absolute;
    left: 308px; top: 56px;
    font-family: "Crimson Text", serif;
    color: var(--white);
    white-space: nowrap;
  }
  .contact-name {
    font-family: "Cinzel", serif;
    font-weight: 500;
    font-size: 16px;
    letter-spacing: .5px;
  }
  .contact-role { color: var(--green); font-size: 15px; margin-bottom: 12px; }
  .contact-list { list-style: none; font-size: 13px; line-height: 1.6; }
  .contact-list li { display: flex; align-items: center; gap: 8px; }
  .contact-list svg { width: 10px; height: 10px; fill: var(--green); flex: none; }
  .contact-list .accent { color: var(--green); }
  .address {
    position: absolute;
    left: 40px; bottom: 34px;
    font-family: "Crimson Text", serif;
    font-size: 16px;
    letter-spacing: .8px;
    color: var(--white);
  }
</style>
</head>
<body>

<section class="card card-front" aria-label="Card front">
  <svg class="card-facets" viewBox="0 0 540 309" preserveAspectRatio="none" aria-hidden="true">
    <polygon points="0,0 300,0 210,120 0,160" fill="var(--facet-1)"/>
    <polygon points="300,0 540,0 540,140 400,90" fill="var(--facet-2)"/>
    <polygon points="400,90 540,140 540,288 460,288" fill="var(--facet-3)" opacity=".6"/>
    <polygon points="210,120 400,90 460,288 260,288" fill="var(--facet-1)"/>
  </svg>
  <div class="brand"><span class="brand-mark"></span>HARGREAVE</div>
  <div class="card-stripe"></div>
</section>

<section class="card card-back" aria-label="Card back">
  <svg class="card-facets" viewBox="0 0 540 309" preserveAspectRatio="none" aria-hidden="true">
    <polygon points="0,0 260,0 180,150 0,120" fill="var(--facet-1)"/>
    <polygon points="260,0 540,0 540,110 280,60" fill="var(--facet-2)"/>
    <polygon points="280,60 540,110 540,288 420,288" fill="var(--facet-3)" opacity=".55"/>
    <polygon points="0,120 180,150 260,288 0,288" fill="var(--facet-1)" opacity=".7"/>
  </svg>
  <div class="brand"><span class="brand-mark"></span>HARGREAVE</div>
  <div class="divider"></div>
  <div class="contact">
    <p class="contact-name">MARTIN HARGREAVE</p>
    <p class="contact-role">Director</p>
    <ul class="contact-list">
      <li><svg viewBox="0 0 24 24"><path d="M6.6 10.8a15.1 15.1 0 0 0 6.6 6.6l2.2-2.2a1 1 0 0 1 1-.25 11.4 11.4 0 0 0 3.6.57 1 1 0 0 1 1 1V20a1 1 0 0 1-1 1A17 17 0 0 1 3 4a1 1 0 0 1 1-1h3.5a1 1 0 0 1 1 1c0 1.25.2 2.45.57 3.6a1 1 0 0 1-.25 1z"/></svg><span>07700 945318</span></li>
      <li><svg viewBox="0 0 24 24"><path d="M2 5h20v14H2zm2 2v.5l8 5 8-5V7z"/></svg><span>martin@hvholdings.co.uk</span></li>
      <li><svg viewBox="0 0 24 24"><circle cx="12" cy="12" r="10"/></svg><span>www.<span class="accent">hargreavehomeholdings</span>.co.uk</span></li>
    </ul>
  </div>
  <p class="address">PO BOX 418, Fernside Road, Larkfield</p>
  <div class="card-stripe"></div>
</section>

</body>
</html>
```